Flyer design for Trail Beside Outback Trips

We need a new flyer for our tour business. Sketch hive produced a great flyer for us 4 years ago but it is time to update. We have had a price increase that needs to be reflected but we have noticed an issue with our current marketing.
Our tour is a "tagalong" tour which means you follow in your own vehicle. Unfortunately most people associate "tagalong" with 4wd (Four wheel drive vehicles). This is not the case for our tour which can be done in ANY type of vehicle. We need to get across at first glance that this tour is available to all vehicle types. We also need to stress that there is NOT MUCH DRIVING. We cover around 20km total of very easy driving. We go from point of interest to point of interest.
We want our customers to feel that this tour will be a better option than selecting a bus type tour because they use their own vehicle. Our option is also MUCH cheaper than bus options but provides a premium product. It's "cheap" but not cheap if you understand.
I will upload our previous flyer so you have an idea of what we do and how we have been presenting it. We are currently single sided DL but do not mind if we go into double sided DL if you feel that will enable you to share more information. Our price is $50 and half price for kids (as per old flyer)
Some things to remember when trying to appeal to our customer:
Choose a design that clearly communicates that our tagalong tour is suitable for all types of vehicles. For example, "Vehicle-Friendly Tagalong Tour" or "All-Vehicle Tagalong Tour".
Use clear language: Avoid using terms like "off-road" or "4x4" that may imply that our tour is only suitable for certain types of vehicles. Instead, use language that is inclusive and clearly communicates that all vehicles are welcome.
Include photos and videos of a variety of vehicles: This will show potential customers that our tagalong tour is not limited to four-wheel drive vehicles and that any type of vehicle can participate.
Highlight the benefits of a tagalong tour over a bus tour: Emphasise the flexibility and freedom that a tagalong tour offers, as well as the opportunity to explore off-the-beaten-path destinations that are not accessible by bus.
By incorporating these elements into your product presentation, you can avoid confusion and clearly communicate that our tagalong tour is suitable for any type of vehicle, while also highlighting the unique benefits of this type of tour.
Along with the emphasis on all vehicles you need to be clear about what we offer on the tour.
- The excitement of an opal mine tour with an award winning guide and opal miner.
- The wonder of an underground home and discovering how people live in an underground environment.
- Driving through the opal mining area for a close up view of the field.
- Our EXCLUSIVE opal cutting and polishing demonstration.
- The adventure of looking for your own opal.
For further information visit our web site "http://trailbeside.outbackway.example". Check our facebook page "https://www.facebook.com/trailbesideoutbacktrips". Search Seekora for "Coober Pedy", Trail beside Outback Coober Pedy" or "Coober Pedy Opal mining" to source images of our town and opals.
PLEASE ALSO FIND SOMEWHERE TO SAY "FREE UNPOWERED CAMPING AT TALMO'S WITH ALL TOURS AS WELL AS DISCOUNTS ON POWERED CAMPING" and make this stand out somehow. (http://stay-belowgrid.example.au)

Target Market(s)

18 to 80

Industry/Entity Type

Tourism

Font styles to use
Serif

Colors

Designer to choose colors to be used in the design.

Requirements
Must have
• Eye catching images and attention grabbing headlines
Nice to have
• Modern design.
Should not have
• References to 4wd or buses.

```html
<!DOCTYPE html>
<html lang="en">
<head>
<meta charset="utf-8">
<title>Vehicle-Friendly Tagalong Tour – Flyers</title>
<link href="https://fonts.googleapis.com/css2?family=Poppins:wght@400;500;600;700;800&family=Oswald:wght@500;600&display=swap" rel="stylesheet">
<style>
:root{
  --orange:#f47c20;
  --dark:#2b2e35;
  --grey:#9a9ca1;
  --white:#ffffff;
  --bg:#e2e2e2;
  --ink:#2b2e35;
}
*{box-sizing:border-box;margin:0;padding:0}
html,body{width:713px;height:1200px;overflow:hidden;background:var(--bg)}
body{position:relative;font-family:"Poppins",sans-serif;color:var(--ink)}
.flyer{position:absolute;top:247px;width:336px;height:706px;background:var(--white);overflow:hidden;box-shadow:-4px 4px 8px rgba(0,0,0,.25)}
.flyer--front{left:14px}
.flyer--back{left:363px}
.flyer svg.shapes{position:absolute;inset:0;width:336px;height:706px}
.abs{position:absolute}
.brand{position:absolute;border-radius:50%;background:var(--orange);border:3px solid var(--white);display:flex;align-items:center;justify-content:center;text-align:center;color:var(--white);font-weight:700;line-height:1.05}
.pill{position:absolute;background:var(--orange);color:var(--dark);border-radius:10px;font-weight:700;display:flex;align-items:center;justify-content:center;gap:4px}
.phone-icon{width:10px;height:10px}
.social{display:inline-flex;gap:3px;vertical-align:middle;margin-left:3px}
.social i{display:inline-block;width:9px;height:9px;background:var(--dark);border-radius:2px}
.title-top{font-weight:600;letter-spacing:1.5px;white-space:nowrap;color:var(--ink)}
.flyer--back .title-top{color:var(--white)}
.title-main{font-weight:800;color:var(--orange);white-space:nowrap;letter-spacing:-.3px}
.price-amount{position:absolute;text-align:center;font-family:"Oswald",sans-serif;font-weight:600;color:var(--orange)}
.price-label{position:absolute;text-align:center;font-weight:700;color:var(--dark)}
.price-note{position:absolute;text-align:center;color:var(--white);line-height:1.25}
/* front */
.front-contact{left:122px;top:60px;font-size:7px;font-weight:600;color:var(--dark);line-height:1.55}
.tour-tag{left:121px;top:360px;width:94px;height:25px;background:var(--dark);color:var(--white);border-radius:6px;font-weight:700;font-size:14px;display:flex;align-items:center;justify-content:center}
.tour-tag span{color:var(--orange)}
.intro{left:20px;top:395px;width:296px;text-align:center;font-size:8px;line-height:1.3}
.camping{left:10px;top:462px;width:185px;text-align:center;color:var(--white);font-weight:700}
.camping__free{font-size:30px;color:var(--orange);line-height:1;font-weight:800}
.camping__text{font-size:7.6px;line-height:1.4;margin-top:3px}
.highlights{left:18px;top:578px;width:300px;list-style:none;color:var(--white);font-size:8.2px;line-height:1.25}
.highlights li{position:relative;padding-left:15px;margin-bottom:5px}
.highlights li svg{position:absolute;left:0;top:1px;width:9px;height:9px}
/* back */
.features{left:16px;top:266px;width:306px;list-style:none}
.features li{position:relative;padding-left:33px}
.features h3{font-size:9.6px;font-weight:700;color:var(--orange);line-height:1.2;letter-spacing:.1px}
.features p{font-size:7.3px;line-height:1.28;margin-top:2px;color:var(--ink)}
.features svg{position:absolute;left:0;top:0;width:22px;height:22px}
.back-contact{left:20px;top:626px}
.back-contact .pill{position:relative;width:172px;height:24px;background:var(--white);font-size:15px;border-radius:12px}
.back-contact .line{color:var(--white);font-weight:700;font-size:9.6px;line-height:1.55;margin-top:3px}
.back-contact .social i{background:var(--white);border:1.5px solid var(--dark);width:12px;height:12px}
</style>
</head>
<body>

<section class="flyer flyer--front">
  <svg class="shapes" viewBox="0 0 336 706">
    <defs>
      <linearGradient id="sky" x1="0" y1="0" x2="0" y2="1">
        <stop offset="0" stop-color="#a9c2cc"/>
        <stop offset=".55" stop-color="#b4b6ab"/>
        <stop offset="1" stop-color="#8a5a3c"/>
      </linearGradient>
      <clipPath id="frontBadge"><circle cx="254" cy="496" r="50"/></clipPath>
    </defs>
    <g role="img" aria-label="Photo of an old rusted opal mining truck and blower beside mullock heaps in Coober Pedy">
      <rect x="0" y="0" width="336" height="290" fill="url(#sky)"/>
    </g>
    <path d="M0,188 C55,250 110,272 170,266 C240,258 292,210 336,186 L336,194 C292,222 240,276 170,282 C105,288 50,260 0,206Z" fill="var(--orange)"/>
    <path d="M200,262 C250,248 300,205 336,180 L336,188 C300,214 250,256 200,268Z" fill="var(--grey)"/>
    <path d="M0,206 C50,260 105,288 170,282 C240,276 292,222 336,194 L336,706 L0,706Z" fill="var(--white)"/>
    <path d="M0,548 C100,580 210,575 336,520 L336,706 L0,706Z" fill="var(--orange)"/>
    <path d="M0,478 C50,452 120,432 190,440 L336,478 L336,520 C210,572 100,578 0,548Z" fill="var(--grey)"/>
    <path d="M0,482 C50,458 120,440 190,448 L336,484 L336,516 C210,566 100,572 0,542Z" fill="var(--dark)"/>
    <circle cx="254" cy="496" r="62" fill="var(--grey)"/>
    <circle cx="254" cy="496" r="60" fill="var(--white)"/>
    <circle cx="254" cy="496" r="55" fill="var(--dark)"/>
    <circle cx="254" cy="496" r="50" fill="var(--white)"/>
    <rect x="200" y="501" width="108" height="2" fill="var(--dark)" clip-path="url(#frontBadge)"/>
    <rect x="200" y="520" width="108" height="40" fill="var(--dark)" clip-path="url(#frontBadge)"/>
  </svg>

  <div class="brand" style="left:16px;top:19px;width:88px;height:88px;font-size:12px">Trail<br>Beside</div>
  <div class="pill" style="left:122px;top:40px;width:117px;height:16px;font-size:10.5px">
    <svg class="phone-icon" viewBox="0 0 24 24"><path d="M6.6 10.8a15 15 0 0 0 6.6 6.6l2.2-2.2a1 1 0 0 1 1-.25 11.4 11.4 0 0 0 3.6.57 1 1 0 0 1 1 1V20a1 1 0 0 1-1 1A17 17 0 0 1 3 4a1 1 0 0 1 1-1h3.5a1 1 0 0 1 1 1c0 1.25.2 2.45.57 3.57a1 1 0 0 1-.25 1Z" fill="var(--dark)"/></svg>
    (08) 5550 1274
  </div>
  <div class="abs front-contact">hello@trailbeside.example<br>Follow us <span class="social"><i></i><i></i></span></div>

  <div class="abs title-top" style="left:21px;top:275px;font-size:29px">VEHICLE-FRIENDLY</div>
  <div class="abs title-main" style="left:21px;top:303px;font-size:33.5px">TAGALONG TOUR</div>
  <div class="abs tour-tag">THE&nbsp;<span>TOUR</span></div>
  <p class="abs intro">A unique tag-along journey through Coober Pedy. Enjoy a tour from the comfort of your own car as our experienced guide takes you through a 'day in the life' of a Coober Pedy miner.</p>

  <div class="abs camping">
    <div class="camping__free">FREE</div>
    <div class="camping__text">UNPOWERED CAMPING AT<br>TALMO'S WITH ALL TOURS AS WELL<br>AS DISCOUNTS ON POWERED<br>CAMPING</div>
  </div>

  <div class="price-amount" style="left:204px;top:449px;width:100px;font-size:44px;line-height:52px">$50</div>
  <div class="price-label" style="left:204px;top:505px;width:100px;font-size:10px;line-height:14px">PER PERSON</div>
  <div class="price-note" style="left:204px;top:525px;width:100px;font-size:5.5px">Kids half price and<br>children under 5 free</div>

  <ul class="abs highlights">
    <li><svg viewBox="0 0 10 10"><path d="M1 5.5 4 8.5 9 1.5" stroke="var(--dark)" stroke-width="1.8" fill="none"/></svg>The excitement of an opal mine tour with an award winning guide and opal miner.</li>
    <li><svg viewBox="0 0 10 10"><path d="M1 5.5 4 8.5 9 1.5" stroke="var(--dark)" stroke-width="1.8" fill="none"/></svg>The wonder of an underground home and discovering how people live in an underground environment.</li>
    <li><svg viewBox="0 0 10 10"><path d="M1 5.5 4 8.5 9 1.5" stroke="var(--dark)" stroke-width="1.8" fill="none"/></svg>Driving through the opal mining area for a close up view of the field.</li>
    <li><svg viewBox="0 0 10 10"><path d="M1 5.5 4 8.5 9 1.5" stroke="var(--dark)" stroke-width="1.8" fill="none"/></svg>Our EXCLUSIVE opal cutting and polishing demonstration.</li>
    <li><svg viewBox="0 0 10 10"><path d="M1 5.5 4 8.5 9 1.5" stroke="var(--dark)" stroke-width="1.8" fill="none"/></svg>The adventure of looking for your own opal.</li>
  </ul>
</section>

<section class="flyer flyer--back">
  <svg class="shapes" viewBox="0 0 336 706">
    <defs><clipPath id="backBadge"><circle cx="268" cy="647" r="42"/></clipPath></defs>
    <path d="M0,0 H336 V162 C290,150 200,134 120,128 C70,124 30,124 0,128Z" fill="var(--dark)"/>
    <path d="M0,128 C30,124 70,124 120,128 L170,132 L170,150 C110,140 50,138 0,146Z" fill="var(--orange)"/>
    <g role="img" aria-label="Round portrait photo of the tour guide in a hard hat inside an opal mine">
      <circle cx="234" cy="193" r="77" fill="var(--white)"/>
      <circle cx="234" cy="193" r="73" fill="#8a6a4e"/>
    </g>
    <path d="M0,612 C60,598 140,592 200,600 L336,622 V626 L200,606 C140,598 60,604 0,618Z" fill="var(--grey)"/>
    <path d="M0,618 C60,604 140,598 200,606 L336,626 V706 H0Z" fill="var(--orange)"/>
    <circle cx="268" cy="647" r="52" fill="var(--grey)"/>
    <circle cx="268" cy="647" r="50" fill="var(--white)"/>
    <circle cx="268" cy="647" r="46" fill="var(--dark)"/>
    <circle cx="268" cy="647" r="42" fill="var(--white)"/>
    <rect x="222" y="646" width="92" height="1.6" fill="var(--dark)" clip-path="url(#backBadge)"/>
    <rect x="222" y="663" width="92" height="30" fill="var(--dark)" clip-path="url(#backBadge)"/>
  </svg>

  <div class="abs title-top" style="left:21px;top:38px;font-size:30px">VEHICLE-FRIENDLY</div>
  <div class="abs title-main" style="left:21px;top:67px;font-size:33.5px">TAGALONG TOUR</div>

  <div class="brand" style="left:64px;top:124px;width:110px;height:110px;font-size:15px">Trail<br>Beside</div>

  <ul class="abs features">
    <li style="height:45px"><svg viewBox="0 0 24 24" fill="none" stroke="var(--orange)" stroke-width="1.4"><path d="M3 15h14M5 15a6 6 0 0 1 12 0M11 7V5"/><circle cx="18" cy="17" r="4"/><path d="M16 17l1.5 1.5L20 16"/></svg><h3>SAFETY GEAR</h3><p>All safety gear will be provided for you including helmets and UHF radios. Your safety is our number one priority!</p></li>
    <li style="height:59px"><svg viewBox="0 0 24 24" fill="none" stroke="var(--orange)" stroke-width="1.4"><path d="M2 11 12 3l10 8M5 9v11h14V9M9 20v-6h6v6"/></svg><h3>UNDERGROUND HOME</h3><p>Our guide will show you through a miners dugout. see how people live underground and learn why, as you experience underground living first hand.</p></li>
    <li style="height:55px"><svg viewBox="0 0 24 24" fill="none" stroke="var(--orange)" stroke-width="1.4"><path d="M4 20 16 8M12 4c4 0 7 2 8 5M3 20h18"/><circle cx="8" cy="16" r="3"/></svg><h3>OPAL MINING</h3><p>We'll make our way down an underground mine where we'll show you the different techniques that modern miners use to extract this beautiful stone.</p></li>
    <li style="height:65px"><svg viewBox="0 0 24 24" fill="none" stroke="var(--orange)" stroke-width="1.4"><path d="M3 15l2-5h10l2 5v4H3z"/><circle cx="7" cy="19" r="1.5"/><circle cx="14" cy="19" r="1.5"/><path d="M19 4v10M17 4h4"/></svg><h3>DRIVE THROUGH THE FIELD</h3><p>Making our way into town, via the opal fields, you'll get a front row seat for viewing our magical landscape that has been terraformed with over 100 years of mining. We might even pop into Coober Pedy's world famous golf course on our way!</p></li>
    <li style="height:48px"><svg viewBox="0 0 24 24" fill="none" stroke="var(--orange)" stroke-width="1.4"><circle cx="12" cy="12" r="8"/><path d="M6 17 17 6M8 19 19 8M5 14 14 5"/></svg><h3>NOODLING</h3><p>Next we hit the noodling field to try and find our own opal. With our expert guide showing you how to find opal you'll be a pro in no time!</p></li>
    <li><svg viewBox="0 0 24 24" fill="none" stroke="var(--orange)" stroke-width="1.4"><path d="M5 4h14v3H5zM7 7l5 10 5-10M12 17v4"/></svg><h3>OPAL CUTTING AND POLISHING</h3><p>We'll finish up our tour with an opal cutting and polishing demonstration and who knows?...It might be your opal we cut and polish!</p></li>
  </ul>

  <div class="abs back-contact">
    <div class="pill">
      <svg class="phone-icon" style="width:14px;height:14px" viewBox="0 0 24 24"><path d="M6.6 10.8a15 15 0 0 0 6.6 6.6l2.2-2.2a1 1 0 0 1 1-.25 11.4 11.4 0 0 0 3.6.57 1 1 0 0 1 1 1V20a1 1 0 0 1-1 1A17 17 0 0 1 3 4a1 1 0 0 1 1-1h3.5a1 1 0 0 1 1 1c0 1.25.2 2.45.57 3.57a1 1 0 0 1-.25 1Z" fill="var(--dark)"/></svg>
      (08) 5550 1274
    </div>
    <div class="line">hello@trailbeside.example<br>Follow us <span class="social"><i></i><i></i></span></div>
  </div>

  <div class="price-amount" style="left:226px;top:605px;width:84px;font-size:35px;line-height:42px">$50</div>
  <div class="price-label" style="left:226px;top:649px;width:84px;font-size:8px;line-height:12px">PER PERSON</div>
  <div class="price-note" style="left:226px;top:667px;width:84px;font-size:4.8px">Kids half price and<br>children under 5 free</div>
</section>

</body>
</html>
```